Digital Marketing Website Design

I need the homepage designed for my new digital marketing agency I am starting. The main goal for this homepage is to drive people to make an appointment for me to discuss their upcoming projects. Here are some examples of the layouts that I would like to emulate.
https://www.tallmarsh.com/
https://www.quillforge.com/
https://pebblenook.com/
https://drvenholt.com/
https://www.quietlyrooted.org/
My main focus is to attract leads that need help with running digital ads such as Chatterly ads and Finder Promos. I do offer other services like SEO and other things but the main focus is digital Ads.
The final design should communicate Orchid Digital is a Digital marketing strategist building predictable revenue for small businesses through digital ads, email and marketing automation.
Target Market(s)
30-55, business owners, income 100K+, ecommerce companies, etc.
Industry/Entity Type
Digital Marketing
Number of Pages Required
2 page
Font styles to use
Requirements
Must have
- An appealing look and feel set to drive people to make an appointment.
Logo
There needs to be a call to action button in the far right of the navigation
The same call to action in the navigation needs to be in each section on the homepage.
I need the homepage and an about us page.

```html
<!DOCTYPE html>
<html lang="en">
<head>
<meta charset="utf-8">
<title>Orchid Digital — Profitable Ad Campaigns</title>
<link href="https://fonts.googleapis.com/css2?family=Poppins:ital,wght@0,400;0,500;0,600;0,700;1,400&display=swap" rel="stylesheet">
<style>
:root{
  --orange:#f5821f;
  --orange-deep:#e9541c;
  --red:#e23b1d;
  --dark:#1d2227;
  --ink:#2b2b2b;
  --muted:#5d5d5d;
  --peach:#fdf1e6;
  --white:#ffffff;
  --line:#e7e7e7;
}
*{margin:0;padding:0;box-sizing:border-box}
html,body{width:1200px;height:2848px;overflow:hidden}
body{font-family:"Poppins",sans-serif;color:var(--ink);background:var(--white);position:relative}
.btn{display:inline-block;font-weight:600;font-size:15px;letter-spacing:.5px;text-transform:uppercase;padding:16px 28px;border-radius:4px}
.btn-orange{background:var(--orange-deep);color:var(--white)}
.btn-white{background:var(--white);color:var(--orange-deep);border:2px solid var(--orange-deep)}

/* hero */
.hero{position:absolute;top:0;left:0;width:1200px;height:660px;overflow:hidden}
.hero-photo{position:absolute;inset:0;background:linear-gradient(100deg,#6b7785 0%,#9aa4ad 35%,#c9a58b 65%,#4c5560 100%)}
.hero-shade{position:absolute;inset:0;background:linear-gradient(180deg,rgba(20,24,30,.55),rgba(20,24,30,.7))}
.nav{position:absolute;top:24px;left:60px;right:60px;display:flex;align-items:center}
.brand{display:flex;align-items:center;gap:10px;font-weight:700;font-size:26px;color:var(--orange);text-transform:uppercase;letter-spacing:1px}
.brand-dot{width:14px;height:14px;border-radius:50%;background:var(--orange)}
.nav-links{margin-left:auto;display:flex;gap:28px;align-items:center;font-size:16px;color:var(--white)}
.nav-links .active{color:var(--orange)}
.nav-links .btn{padding:14px 22px;font-size:14px;margin-left:14px}
.hero-copy{position:absolute;top:250px;left:0;width:1200px;text-align:center;color:var(--white)}
.hero-copy h1{font-size:52px;font-weight:700;line-height:1.18}
.hero-copy p{font-size:18px;line-height:1.55;margin:18px auto 0;width:560px;color:#eef0f2}
.hero-ctas{margin-top:34px;display:flex;gap:20px;justify-content:center}

/* partners */
.partners{position:absolute;top:680px;left:0;width:1200px;height:120px;display:flex;align-items:center;justify-content:center;gap:50px;font-size:28px;font-weight:600;color:#31507a;border-bottom:1px solid var(--line)}
.partners span{display:flex;align-items:center;gap:10px;white-space:nowrap}
.partners i{width:18px;height:18px;border-radius:50%;background:#31507a;display:inline-block}

/* how it work */
.how-band{position:absolute;top:820px;left:0;width:1200px;height:600px;background:var(--peach)}
.section-title{position:absolute;left:0;width:1200px;text-align:center;font-size:50px;font-weight:700;color:var(--dark);text-transform:uppercase}
.how-intro{position:absolute;top:960px;left:180px;width:840px;text-align:center;font-size:15px;line-height:1.7;color:var(--muted)}
.how-intro p+p{margin-top:14px}
.how-visual{position:absolute;top:1190px;left:330px;width:540px;height:370px;border-radius:6px;background:linear-gradient(160deg,#f4f4f4,#d9dde1 55%,#f19a4a)}
.steps-line{position:absolute;top:1676px;left:270px;width:660px;height:3px;background:#f1c6a3}
.step{position:absolute;top:1640px;width:260px;text-align:center}
.step-num{width:72px;height:72px;margin:0 auto;border-radius:50%;background:var(--orange-deep);color:var(--white);font-size:28px;font-weight:700;display:flex;align-items:center;justify-content:center;box-shadow:0 0 0 8px #fbd9bf}
.step p{margin-top:34px;font-size:15px;line-height:1.6;color:var(--muted)}
.how-outro{position:absolute;top:1905px;left:300px;width:600px;text-align:center;font-size:16px;font-style:italic;line-height:1.7;color:var(--muted)}

/* testimonials */
.testimonials{position:absolute;top:2060px;left:0;width:1200px;height:520px;overflow:hidden}
.testimonials-photo{position:absolute;inset:0;background:linear-gradient(120deg,#3a3f46,#5a4c40 50%,#2c3036)}
.testimonials-shade{position:absolute;inset:0;background:rgba(20,22,26,.55)}
.testimonials .section-title{top:50px;color:var(--white);font-size:46px}
.card{position:absolute;top:140px;width:318px;height:340px;background:var(--white);border-radius:6px;padding:28px 28px}
.avatar{width:96px;height:96px;border-radius:50%;background:linear-gradient(160deg,#e7d3c2,#a88872);border:4px solid #f3e3d6}
.card p{margin-top:36px;font-size:15px;line-height:1.6;color:var(--muted)}
.card h4{margin-top:18px;font-size:18px;font-weight:600;color:var(--dark)}

/* footer */
.footer{position:absolute;top:2580px;left:0;width:1200px;height:268px;background:linear-gradient(180deg,var(--orange) 0%,var(--red) 100%);color:var(--white);padding:30px 80px}
.footer-cols{display:flex;gap:70px}
.footer-col h5{font-size:22px;font-weight:600;text-transform:uppercase;margin-bottom:16px}
.footer-col li{list-style:none;font-size:13px;line-height:1.9;display:flex;gap:8px;align-items:flex-start}
.footer-brand{width:260px;padding-top:50px}
.footer-brand .brand{color:var(--white);font-size:24px}
.footer-brand .brand-dot{background:var(--white)}
.footer-brand p{margin-top:10px;font-size:13px;line-height:1.6}
.socials{display:flex;gap:10px;margin-top:8px}
.socials span{width:34px;height:34px;border:2px solid var(--white);border-radius:50%}
.quick li::before{content:"";width:6px;height:6px;border-radius:50%;background:var(--white);margin-top:9px;flex:none}
</style>
</head>
<body>

<header class="hero">
  <div class="hero-photo" role="img" aria-label="Smiling business team working together in a bright office"></div>
  <div class="hero-shade"></div>
  <nav class="nav">
    <div class="brand"><span class="brand-dot"></span>Orchid Digital</div>
    <div class="nav-links">
      <span class="active">Home</span><span>How It Work</span><span>Contact</span>
      <span class="btn btn-orange">Schedule Appointment</span>
    </div>
  </nav>
  <div class="hero-copy">
    <h1>We Built Profitable Ad Campaigns<br>For small businesses</h1>
    <p>The selling system that brings in Predictable revenue through digital ads, email, and marketing automation.</p>
    <div class="hero-ctas">
      <span class="btn btn-orange">Free Chatterly Ads</span>
      <span class="btn btn-white">Schedule Appointment</span>
    </div>
  </div>
</header>

<section class="partners">
  <span><i></i>Plinth</span><span>Notions</span><span>Chatterly</span><span>Finder Promos</span><span>Kovra</span><span>Tunewell</span>
</section>

<section>
  <div class="how-band"></div>
  <h2 class="section-title" style="top:870px">How It Work</h2>
  <div class="how-intro">
    <p>At Orchid Digital Solutions we know that you want to have a profitable business. In order to do that, you need a strong system that can predictably bring in sales even in bad times. The problem is there is so much out there to wade through and so many people telling you what you should do which makes you feel frustrated, lost, and flat out stressed out. We believe that businesses with great products should get the customers.</p>
    <p>We understand the frustration which is why we are here to help you maneuver through the minutiae and create a system that flat out works.</p>
  </div>
  <div class="how-visual" role="img" aria-label="Laptop showing a small business idea illustration"></div>
  <div class="steps-line"></div>
  <div class="step" style="left:140px"><div class="step-num">1</div><p>Schedule an appointment to go through the basics of what you need and to find out if we are a good fit to work together</p></div>
  <div class="step" style="left:470px"><div class="step-num">2</div><p>Work with our team to build out your customer journey and selling system</p></div>
  <div class="step" style="left:800px"><div class="step-num">3</div><p>Execute and enjoy the extra revenue</p></div>
  <p class="how-outro">So, schedule your appointment today. And in the meantime checkout our Chatterly ads checklist. So you can stop any poor running campaigns and fill in the gaps where they are needed.</p>
</section>

<section class="testimonials">
  <div class="testimonials-photo" role="img" aria-label="Team meeting in a dim modern office"></div>
  <div class="testimonials-shade"></div>
  <h2 class="section-title">What Other Are Saying</h2>
  <div class="card" style="left:80px"><div class="avatar" role="img" aria-label="Client portrait"></div><p>Lorem ipsum is simply dummy text of the printing and typesetting in industry lorem ipsum.</p><h4>Client Name</h4></div>
  <div class="card" style="left:441px"><div class="avatar" role="img" aria-label="Client portrait"></div><p>Lorem ipsum is simply dummy text of the printing and typesetting in industry lorem ipsum.</p><h4>Client Name</h4></div>
  <div class="card" style="left:802px"><div class="avatar" role="img" aria-label="Client portrait"></div><p>Lorem ipsum is simply dummy text of the printing and typesetting in industry lorem ipsum.</p><h4>Client Name</h4></div>
</section>

<footer class="footer">
  <div class="footer-cols">
    <div class="footer-brand">
      <div class="brand"><span class="brand-dot"></span>Orchid Digital</div>
      <p>Orchid Digital – 2020. All rights reserved.</p>
    </div>
    <div class="footer-col" style="width:220px">
      <h5>Address</h5>
      <ul>
        <li><svg width="14" height="18" viewBox="0 0 14 18"><path d="M7 0a7 7 0 0 0-7 7c0 5 7 11 7 11s7-6 7-11a7 7 0 0 0-7-7zm0 10a3 3 0 1 1 0-6 3 3 0 0 1 0 6z" fill="#fff"/></svg><span>OrchidDigital<br>70 – Lorem ipsum street,<br>text print type text</span></li>
      </ul>
      <div class="socials"><span></span><span></span></div>
    </div>
    <div class="footer-col" style="width:230px">
      <h5>Contact Info</h5>
      <ul>
        <li><svg width="16" height="16" viewBox="0 0 16 16"><path d="M3 1l3 3-2 2a10 10 0 0 0 6 6l2-2 3 3-2 2C6 15 1 10 1 3z" fill="#fff"/></svg><span>Phone:<br>(123) 456-7890</span></li>
        <li><svg width="16" height="12" viewBox="0 0 16 12"><rect x="1" y="1" width="14" height="10" fill="none" stroke="#fff" stroke-width="1.5"/><path d="M1 1l7 6 7-6" fill="none" stroke="#fff" stroke-width="1.5"/></svg><span>Email:<br>info@orchiddigital.com</span></li>
      </ul>
    </div>
    <div class="footer-col quick">
      <h5>Quicklinks</h5>
      <ul><li>Terms of Service</li><li>Privacy Policy</li><li>Appointment Navigation</li><li>Regular content</li><li>Case studies</li></ul>
    </div>
  </div>
</footer>

</body>
</html>
```